Stationery for Public Accountant Practice

Name of Practice
Holloway Merrick Pty Ltd
Tel: 0413927056
Postal Address : PO Box 482, Oakvale East, Vic 3187

Target Market(s)

Small Business Clients

Industry/Entity Type

Accounting

Font styles to use
Serif

Requirements
Must have
• Letterhead, business card, With compliments slip
Nice to have
• Conservative

```html
<!DOCTYPE html>
<html lang="en">
<head>
<meta charset="utf-8">
<title>Holloway Merrick Pty Ltd — Stationery</title>
<link href="https://fonts.googleapis.com/css2?family=Lato:ital,wght@0,400;0,700;0,900;1,700&family=Tinos:wght@400&display=swap" rel="stylesheet">
<style>
  :root {
    --blue: #1d73c4;
    --blue-deep: #0f4fa8;
    --blue-light: #3c8fd9;
    --ink: #1a1a1a;
    --paper: #ffffff;
    --backdrop: #d8d9db;
    --band: #111111;
  }
  * { box-sizing: border-box; margin: 0; padding: 0; }
  html, body { width: 860px; height: 1200px; overflow: hidden; }
  body { background: var(--backdrop); font-family: "Lato", Arial, sans-serif; color: var(--ink); }
  .canvas { position: relative; width: 860px; height: 1200px; }

  .sheet { position: absolute; background: var(--paper); overflow: hidden; box-shadow: 0 2px 6px rgba(0,0,0,.18); }

  /* wordmark */
  .brand { display: flex; align-items: center; gap: 7px; }
  .brand-square { width: 22px; height: 22px; background: var(--blue); flex: none; }
  .brand-name { font-weight: 900; color: var(--blue); font-size: 14px; line-height: 1.05; letter-spacing: .5px; text-transform: uppercase; white-space: nowrap; }
  .brand.light .brand-square { background: var(--paper); }
  .brand.light .brand-name { color: var(--paper); }

  /* footer band */
  .footer-bar { position: absolute; left: 0; right: 0; bottom: 0; height: 6px; background: var(--band); }
  .footer-tab { position: absolute; right: 0; bottom: 0; height: 18px; width: 150px; background: var(--blue);
    clip-path: polygon(12px 0, 100% 0, 100% 100%, 0 100%);
    color: var(--paper); font-weight: 700; font-style: italic; font-size: 8px;
    display: flex; align-items: center; justify-content: center; padding-left: 10px; }

  /* letterhead back */
  .letterhead-back { left: 30px; top: 30px; width: 380px; height: 537px;
    background: radial-gradient(ellipse at 35% 45%, var(--blue-light) 0%, var(--blue) 45%, var(--blue-deep) 100%); }
  .letterhead-back .brand { position: absolute; left: 40px; top: 240px; }
  .letterhead-back .brand-square { width: 28px; height: 28px; }
  .letterhead-back .brand-name { font-size: 17px; }

  /* letterhead front */
  .letterhead { left: 450px; top: 30px; width: 380px; height: 537px; }
  .letterhead .brand { position: absolute; left: 20px; top: 24px; }
  .letterhead .brand-square { width: 20px; height: 20px; }
  .letterhead .brand-name { font-size: 11px; }
  .letterhead-rule { position: absolute; left: 196px; right: 0; top: 16px; height: 2px; background: var(--blue); }
  .contact-block { position: absolute; left: 204px; top: 24px; font-size: 6.5px; line-height: 1.6; white-space: nowrap; }
  .contact-block .label { color: var(--blue); font-weight: 700; }
  .letter { position: absolute; left: 32px; top: 98px; width: 300px; font-family: "Tinos", "Times New Roman", serif; font-size: 7.4px; line-height: 1.3; }
  .letter p { margin-bottom: 8px; }

  /* business cards */
  .card { width: 380px; height: 217px; top: 600px; }
  .card-back { left: 30px;
    background: radial-gradient(ellipse at 40% 40%, var(--blue-light) 0%, var(--blue) 50%, var(--blue-deep) 100%); }
  .card-back .brand { position: absolute; left: 110px; top: 94px; }
  .card-back .brand-square { width: 26px; height: 26px; }
  .card-back .brand-name { font-size: 15px; }
  .card-front { left: 450px; }
  .card-front .brand { position: absolute; left: 20px; top: 76px; }
  .card-front .brand-square { width: 26px; height: 26px; }
  .card-front .brand-name { font-size: 12px; }
  .card-divider { position: absolute; left: 216px; top: 42px; width: 1px; height: 110px; background: var(--ink); }
  .card-details { position: absolute; left: 228px; top: 52px; font-size: 10px; line-height: 1.35; white-space: nowrap; }
  .person-name { color: var(--blue); font-size: 15px; line-height: 1.15; }
  .person-role { margin-bottom: 12px; }
  .card-details .label { color: var(--blue); }
  .card-front .footer-bar { height: 10px; }
  .card-front .footer-tab { width: 190px; height: 24px; font-size: 10px; }

  /* envelope */
  .envelope { left: 30px; top: 850px; width: 380px; height: 190px; }
  .envelope svg { position: absolute; inset: 0; }
  .envelope .flap-mark { position: absolute; left: 182px; top: 16px; width: 16px; height: 16px; background: var(--blue); }

  /* compliments slip */
  .comp-slip { left: 450px; top: 850px; width: 380px; height: 190px; }
  .comp-slip .brand { position: absolute; left: 20px; top: 24px; }
  .comp-slip .brand-name { font-size: 13px; }
  .comp-title { position: absolute; right: 22px; top: 30px; font-weight: 700; font-style: italic; font-size: 10px; }
  .comp-contact { position: absolute; left: 20px; bottom: 26px; font-size: 6.5px; line-height: 1.5; }
  .comp-contact .label { color: var(--blue); font-weight: 700; }
</style>
</head>
<body>
<main class="canvas">

  <section class="sheet letterhead-back" role="img" aria-label="Blue letterhead reverse with soft tonal gradient">
    <div class="brand light">
      <span class="brand-square"></span>
      <span class="brand-name">Holloway Merrick<br>Pty Ltd</span>
    </div>
  </section>

  <section class="sheet letterhead">
    <div class="letterhead-rule"></div>
    <div class="brand">
      <span class="brand-square"></span>
      <span class="brand-name">Holloway Merrick<br>Pty Ltd</span>
    </div>
    <div class="contact-block">
      <div><span class="label">Address :</span> PO Box 482, Oakvale East, Vic 3187</div>
      <div><span class="label">Tel :</span> 0413927056</div>
    </div>
    <article class="letter">
      <p>May 30, 2006</p>
      <p>Maria Conlan<br>4127 Harbour Lane<br>Geelong, VIC 3220</p>
      <p>Dear Ms. Conlan:</p>
      <p>Thank you for choosing our practice for your annual accounts.</p>
      <p>Our team has reviewed the records you supplied for the last financial year. Your statements are now complete and ready for your review, and we have noted several areas where your business may reduce its tax position.</p>
      <p>We would welcome a short meeting to discuss these points and to plan for the coming year. Please contact our office at a time that suits you.</p>
      <p>We look forward to working with you again.</p>
      <p>Regards,</p>
      <p>Ruth Keane</p>
    </article>
    <div class="footer-bar"></div>
    <div class="footer-tab">Holloway Merrick Pty Ltd</div>
  </section>

  <section class="sheet card card-back" role="img" aria-label="Business card reverse, blue tonal gradient with company name">
    <div class="brand light">
      <span class="brand-square"></span>
      <span class="brand-name">Holloway Merrick<br>Pty Ltd</span>
    </div>
  </section>

  <section class="sheet card card-front">
    <div class="brand">
      <span class="brand-square"></span>
      <span class="brand-name">Holloway Merrick<br>Pty Ltd</span>
    </div>
    <div class="card-divider"></div>
    <div class="card-details">
      <div class="person-name">Daniel Ashworth</div>
      <div class="person-role">Manager</div>
      <div><span class="label">A :</span> PO Box 482, Oakvale<br>East, Vic 3187</div>
      <div><span class="label">T :</span> 0413927056</div>
    </div>
    <div class="footer-bar"></div>
    <div class="footer-tab">Holloway Merrick Pty Ltd</div>
  </section>

  <section class="sheet envelope">
    <svg width="380" height="190" viewBox="0 0 380 190" aria-hidden="true">
      <defs>
        <linearGradient id="flapShade" x1="0" y1="0" x2="0" y2="1">
          <stop offset="0" stop-color="#1d73c4"/>
          <stop offset="1" stop-color="#7fb4e6"/>
        </linearGradient>
      </defs>
      <path d="M0 0 H380 V8 L210 58 Q190 64 170 58 L0 8 Z" fill="url(#flapShade)"/>
      <path d="M0 8 L170 58 Q190 64 210 58 L380 8" fill="none" stroke="#c9d9ea" stroke-width="1"/>
    </svg>
    <span class="flap-mark"></span>
  </section>

  <section class="sheet comp-slip">
    <div class="brand">
      <span class="brand-square"></span>
      <span class="brand-name">Holloway Merrick<br>Pty Ltd</span>
    </div>
    <div class="comp-title">With Compliments</div>
    <div class="comp-contact">
      <div><span class="label">Tel :</span> 0413927056</div>
      <div><span class="label">Address :</span> PO Box 482, Oakvale East, Vic 3187</div>
    </div>
    <div class="footer-bar"></div>
    <div class="footer-tab">Holloway Merrick Pty Ltd</div>
  </section>

</main>
</body>
</html>
```